Create a dynamisch, inspiring PowerPoint Design master for our company Brightway & Partners

Core business: Coaching, Consulting and Executive search

The PPT master should be easy to use and include professional formatting (using the fonts of our website). In general, the slide master should have the look and feel of our website (in terms of fonts, colors, logos) We also would like to place big photographs on some slides, having text and graph slides as well as photo slides with just 1 key message or a citation.

The PowerPoint design should fit our corporate Identity www.brightway-partners.de
I have enclosed the PPT we use now.

Logos und colors are attached, also the master PPD we now use. We need the new master to be more modern, dynamisch und nicht so dreary, grey, but far more attractive and inspiring. If necessary we ca add a new color to make it more attractive. Please advise.

Additional information:
- wide screen format - 16:9
- creation of chart templates, using chart tools, and different chart types etc.
- creation of different slide layouts to place content, pictures (in different sizes), optionally Media
- as well as standard elements, such as text boxes, lines, default shapes, etc.

We have received your contact info and recommondations from Renate Kolbeck-Strauss. We liked the master you designed very much and would like that kind of style. I can send you her presentation as a reminder if needed?

```html
<!DOCTYPE html>
<html lang="en">
<head>
<meta charset="utf-8">
<title>Brightway &amp; Partners – Presentation Master</title>
<link rel="stylesheet" href="https://fonts.googleapis.com/css2?family=Comfortaa:wght@400;600;700&family=Open+Sans:wght@400;600;700&display=swap">
<style>
:root{
  --teal:#0f7f78;
  --teal-dark:#0b5f5a;
  --teal-deep:#094b47;
  --teal-light:#8fcac4;
  --teal-pale:#d8eeeb;
  --coral:#f36b4b;
  --grey:#6d6d6d;
  --grey-light:#d9d9d9;
  --ink:#3a3a3a;
  --text:#8a8a8a;
  --canvas:#a9a9a9;
  --white:#ffffff;
}
*{box-sizing:border-box;margin:0;padding:0}
html,body{width:1200px;height:2721px;overflow:hidden;background:var(--canvas)}
body{font-family:"Open Sans",Arial,sans-serif;color:var(--ink)}
.sheet{display:grid;grid-template-columns:repeat(3,390px);grid-template-rows:repeat(12,219.5px);gap:6px;padding:9px}
.slide{position:relative;overflow:hidden;background:var(--white)}
.abs{position:absolute}
.photo{position:absolute}
.display{font-family:"Comfortaa",Arial,sans-serif;font-weight:600}
.h-title{position:absolute;font-family:"Comfortaa",Arial,sans-serif;font-size:14.5px;font-weight:600;color:var(--ink)}
.h-title::after{content:"";display:block;width:16px;height:2px;background:var(--teal);margin-top:5px}
.h-title.light{color:var(--white)}
.h-title.light::after{background:var(--white)}
.body{font-size:4.4px;line-height:1.5;color:var(--text)}
.body.w{color:rgba(255,255,255,.9)}
.label{font-size:4.8px;font-weight:600;color:var(--ink)}
.label.w{color:var(--white)}
.label.t{color:var(--teal)}
.foot-bar{position:absolute;left:0;bottom:4px;width:3px;height:10px;background:var(--teal)}
.foot-mark{position:absolute;left:7px;bottom:5px;font-family:"Comfortaa",Arial,sans-serif;font-weight:700;font-size:6px;color:var(--teal)}
.foot-mark.w{color:var(--white)}
.page-no{position:absolute;right:10px;bottom:6px;font-size:3.4px;letter-spacing:.8px;color:#9a9a9a}
.page-no.w{color:rgba(255,255,255,.7)}
.brand{font-family:"Comfortaa",Arial,sans-serif;font-weight:600;color:var(--grey);line-height:1.1}
.brand small{display:block;font-size:.33em;letter-spacing:.4px;margin-top:2px}
.icon-dot{position:absolute;width:18px;height:18px;border-radius:50%;background:var(--teal-dark);border:2px solid var(--teal-pale)}
.card{position:absolute;background:var(--white);border-radius:3px;box-shadow:0 1px 3px rgba(0,0,0,.18)}
.rounded{border-radius:10px}
.tile{position:absolute;background:var(--teal);border-radius:4px}
</style>
</head>
<body>
<main class="sheet">

<!-- 1 cover -->
<section class="slide">
  <div class="photo" role="img" aria-label="Classical building facade tinted teal" style="inset:0;background:linear-gradient(150deg,#3b958d,#0e6f68 60%,#0b5f5a)"></div>
  <svg class="abs" style="inset:0" width="390" height="219.5" viewBox="0 0 390 219.5"><path d="M0 219.5 L0 202 C130 200 300 160 390 38 L390 219.5 Z" fill="#fff"/></svg>
  <div class="abs display" style="left:30px;top:82px;color:#fff;font-size:16.5px;line-height:1.4">Your title goes here<br>One-two sentences</div>
  <div class="abs brand" style="right:14px;top:184px;font-size:13px;text-align:right">Brightway &amp; Partners<small>COACHING, CONSULTING UND EXECUTIVE SEARCH</small></div>
</section>

<!-- 2 cover circles -->
<section class="slide">
  <div class="photo" role="img" aria-label="Black and white classical building facade" style="inset:0;background:linear-gradient(160deg,#f2f2f2,#c9c9c9 55%,#e6e6e6)"></div>
  <svg class="abs" style="inset:0" width="390" height="219.5"><circle cx="160" cy="110" r="52" fill="#0f7f78" fill-opacity=".55"/><circle cx="230" cy="118" r="52" fill="#0f7f78" fill-opacity=".55"/></svg>
  <div class="abs display" style="left:0;right:0;top:92px;text-align:center;color:var(--ink);font-size:21px;line-height:1">Your title goes here<div style="font-size:13px;margin-top:2px">One-two sentences</div></div>
</section>

<!-- 3 cover circles light -->
<section class="slide">
  <div class="photo" role="img" aria-label="Black and white classical building facade" style="inset:0;background:linear-gradient(160deg,#f6f6f6,#d5d5d5 55%,#ededed)"></div>
  <svg class="abs" style="inset:0" width="390" height="219.5"><circle cx="160" cy="110" r="52" fill="#8fcac4" fill-opacity=".55"/><circle cx="230" cy="118" r="52" fill="#8fcac4" fill-opacity=".55"/></svg>
  <div class="abs display" style="left:0;right:0;top:92px;text-align:center;color:var(--ink);font-size:21px;line-height:1">Your title goes here<div style="font-size:13px;margin-top:2px">One-two sentences</div></div>
</section>

<!-- 4 photo cover -->
<section class="slide">
  <div class="photo" role="img" aria-label="Sunrise over green mountain landscape under dramatic clouds" style="left:0;top:0;width:390px;height:172px;background:linear-gradient(180deg,#4d6da3,#a9a7a5 45%,#e8c16a 60%,#4e6b3a 80%,#3f5d2c)"></div>
  <div class="abs display" style="left:18px;top:180px;font-size:12px;color:var(--ink);line-height:1.05">YOUR TITLE GOES HERE<div style="font-size:10px">One-two sentences</div></div>
  <div class="abs brand" style="right:14px;top:186px;font-size:11px;text-align:right">Brightway &amp; Partners<small>COACHING, CONSULTING UND EXECUTIVE SEARCH</small></div>
</section>

<!-- 5 section divider photo -->
<section class="slide">
  <div class="photo" role="img" aria-label="Coastline with cliffs, trees and ocean waves" style="inset:0;background:linear-gradient(180deg,#c9d6dc,#7d99a1 35%,#3f6c73 60%,#5c7a3d)"></div>
  <svg class="abs" style="inset:0" width="390" height="219.5"><path d="M0 160 C120 185 260 190 390 150 L390 219.5 L0 219.5 Z" fill="#0f7f78"/></svg>
  <div class="abs display" style="left:18px;top:180px;color:#fff;font-size:12px">SECTION DIVIDER<div style="font-size:4.5px;letter-spacing:1.2px;opacity:.8">SECTION SUBTITLE</div></div>
  <div class="abs brand" style="right:12px;top:204px;font-size:5.5px;color:#fff">Brightway &amp; Partners</div>
</section>

<!-- 6 section divider teal -->
<section class="slide" style="background:linear-gradient(180deg,#7fc2bb,#4ea49c)">
  <svg class="abs" style="inset:0" width="390" height="219.5"><path d="M0 160 C120 185 260 190 390 150 L390 219.5 L0 219.5 Z" fill="#0f7f78"/></svg>
  <div class="abs display" style="left:18px;top:180px;color:#fff;font-size:12px">SECTION DIVIDER<div style="font-size:4.5px;letter-spacing:1.2px;opacity:.8">SECTION SUBTITLE</div></div>
  <div class="abs brand" style="right:12px;top:204px;font-size:5.5px;color:#fff">Brightway &amp; Partners</div>
</section>

<!-- 7 agenda -->
<section class="slide">
  <div class="abs" style="left:0;top:0;width:146px;height:219.5px;background:var(--teal)"></div>
  <div class="abs display" style="left:38px;top:100px;color:#fff;font-size:13px">AGENDA</div>
  <div class="abs brand" style="left:38px;top:200px;font-size:5.5px;color:#fff">Brightway &amp; Partners</div>
  <div class="abs" style="left:126px;top:56px;width:204px">
    <div style="display:grid;grid-template-columns:24px 1fr;font-size:6px;color:var(--grey)">
      <span style="padding:3px 0">01</span><span style="padding:3px 0;border-bottom:.5px solid #ccc">Introduction - Welcome</span>
      <span style="padding:3px 0">02</span><span style="padding:3px 0;border-bottom:.5px solid #ccc">Mission &amp; Vision</span>
      <span style="padding:3px 0">03</span><span style="padding:3px 0;border-bottom:.5px solid #ccc">Our Services</span>
      <span style="padding:3px 0">04</span><span style="padding:3px 0;border-bottom:.5px solid #ccc">Company Profile</span>
      <span style="padding:3px 0">05</span><span style="padding:3px 0;border-bottom:.5px solid #ccc">Project Portfolio</span>
      <span style="padding:3px 0">06</span><span style="padding:3px 0;border-bottom:.5px solid #ccc">Our Team</span>
      <span style="padding:3px 0">07</span><span style="padding:3px 0;border-bottom:.5px solid #ccc">Our Offices</span>
      <span style="padding:3px 0">08</span><span style="padding:3px 0;border-bottom:.5px solid #ccc">Q&amp;As / Closing Speech</span>
    </div>
  </div>
  <div class="page-no">PAGE | 3</div>
</section>

<!-- 8 profile -->
<section class="slide">
  <div class="abs" style="left:0;top:0;width:100px;height:219.5px;background:var(--teal)"></div>
  <div class="photo" role="img" aria-label="Round portrait photo of two business partners" style="left:32px;top:48px;width:120px;height:120px;border-radius:50%;border:4px solid #fff;background:radial-gradient(circle at 50% 40%,#e6e6e6,#9a9a9a 70%,#5d5d5d)"></div>
  <div class="abs display" style="left:128px;top:48px;width:150px;height:16px;border-radius:8px;background:var(--grey);color:#fff;font-size:9px;padding:3px 0 0 24px">Your Name</div>
  <p class="abs body" style="left:172px;top:80px;width:196px">Lorem ipsum dolor sit amet, consectetur adipiscing elit, sed do eiusmod tempor incididunt ut labore et dolore magna aliqua. Ut enim ad minim veniam, quis nostrud exercitation ullamco laboris nisi ut aliquip ex ea commodo consequat. Duis aute irure dolor in reprehenderit in voluptate velit esse cillum.<br><br>Lorem ipsum dolor sit amet, consectetur adipiscing elit, sed do eiusmod tempor incididunt ut labore et dolore magna aliqua. Ut enim ad minim veniam, quis nostrud exercitation ullamco laboris nisi ut aliquip.</p>
  <div class="page-no">PAGE | 4</div>
</section>

<!-- 9 heading text image -->
<section class="slide">
  <div class="photo" role="img" aria-label="Coaching session in a bright office, black and white" style="left:0;top:0;width:220px;height:145px;background:linear-gradient(120deg,#d8d8d8,#a5a5a5 50%,#eeeeee)"></div>
  <div class="photo" role="img" aria-label="Door sign reading coaching room occupied" style="left:220px;top:0;width:170px;height:60px;background:linear-gradient(180deg,#f1f1f1,#dcdcdc)"></div>
  <div class="abs rounded" style="left:213px;top:56px;width:104px;height:95px;background:var(--teal);padding:10px 14px;color:#fff">
    <div class="display" style="font-size:18px;opacity:.35;line-height:1">01</div>
    <div class="label w" style="margin-top:-8px;font-size:5.5px">Your Text Here</div>
    <p class="body w" style="margin-top:6px;font-size:4px">Lorem ipsum dolor sit amet, consectetur adipiscing elit, sed do eiusmod tempor incididunt ut labore et dolore magna aliqua.</p>
  </div>
  <div class="abs display" style="left:24px;top:164px;font-size:15px;color:var(--ink)">Heading + Text + Image Slide</div>
  <div class="foot-bar"></div><div class="foot-mark">Brightway</div><div class="page-no">PAGE | 5</div>
</section>

<!-- 10 title + badge -->
<section class="slide">
  <div class="h-title" style="left:30px;top:52px">Here Add Your Title</div>
  <p class="abs body" style="left:30px;top:80px;width:152px">Lorem ipsum dolor sit amet, consectetur adipiscing elit, sed do eiusmod tempor incididunt ut labore et dolore magna aliqua. Ut enim ad minim veniam, quis nostrud exercitation ullamco laboris nisi ut aliquip consequat.</p>
  <ul class="abs body" style="left:36px;top:120px;width:150px">
    <li>Lorem ipsum dolor sit amet consectetur adipiscing</li><li>Sed do eiusmod tempor incididunt ut labore</li><li>Dolore magna aliqua ut enim ad minim veniam</li><li>Quis nostrud exercitation ullamco laboris</li><li>Nisi ut aliquip ex ea commodo consequat</li>
  </ul>
  <div class="photo" role="img" aria-label="Round photo of a smiling woman holding a smiley balloon" style="left:205px;top:38px;width:132px;height:132px;border-radius:50%;background:radial-gradient(circle at 40% 40%,#f7e3b5,#d8b47a 55%,#b8b8b8)"></div>
  <div class="abs" style="left:298px;top:46px;width:52px;height:52px;border-radius:50%;background:var(--teal);border:3px solid #fff;color:#fff;text-align:center;padding-top:9px">
    <div class="display" style="font-size:13px;line-height:1">+18</div><div style="font-size:4.5px;font-weight:700;color:var(--coral)">AWESOME</div><div style="font-size:3.5px">TEXT HERE</div>
  </div>
  <div class="foot-bar"></div><div class="foot-mark">Brightway</div><div class="page-no">PAGE | 10</div>
</section>

<!-- 11 group quote -->
<section class="slide">
  <div class="photo" role="img" aria-label="Black and white group photo of the team in a bright room" style="left:0;top:0;width:390px;height:140px;background:linear-gradient(180deg,#cfcfcf,#8d8d8d 55%,#f3f3f3)"></div>
  <div class="abs" style="left:187px;top:131px;width:14px;height:14px;border-radius:50%;background:var(--teal);color:#fff;font-size:10px;text-align:center;line-height:16px;font-weight:700">&#8220;</div>
  <p class="abs body" style="left:70px;top:150px;width:250px;text-align:center;color:var(--ink);font-size:5.3px">Lorem ipsum dolor sit amet, consectetur adipiscing elit. Lorem ipsum dolor sit amet, consectetur adipiscing elit, sed do eiusmod tempor incididunt ut labore et dolore magna aliqua.</p>
  <div class="abs label t" style="left:0;right:0;top:178px;text-align:center">Your Name</div>
  <div class="foot-bar"></div><div class="foot-mark">Brightway</div><div class="page-no">PAGE | 11</div>
</section>

<!-- 12 puzzle quote -->
<section class="slide">
  <div class="photo" role="img" aria-label="White jigsaw puzzle with one grey piece being placed" style="left:0;top:0;width:200px;height:219.5px;background:linear-gradient(120deg,#f7f7f7,#dcdcdc 50%,#f4f4f4)"></div>
  <div class="abs" style="left:212px;top:62px;width:12px;height:12px;border-radius:50%;background:var(--teal);color:#fff;font-size:9px;text-align:center;line-height:14px;font-weight:700">&#8220;</div>
  <p class="abs" style="left:212px;top:80px;width:160px;font-size:5.6px;line-height:1.55;color:var(--ink)">… we find the right candidates for you<br>… we evaluate your management team<br>… we lift and develop the competencies within your organization<br>… we work with your problems and potential on an individual level</p>
  <div class="abs label t" style="left:212px;top:134px">Your Name</div>
  <div class="page-no">PAGE | 12</div>
</section>

<!-- 13 about us -->
<section class="slide">
  <div class="h-title" style="left:38px;top:58px">About Us</div>
  <p class="abs" style="left:38px;top:86px;width:115px;font-size:4.8px;font-weight:600;color:var(--ink)">No problem is too big or too small!<br>We're here to help.</p>
  <p class="abs body" style="left:38px;top:104px;width:115px;text-align:justify">Lorem ipsum dolor sit amet, consectetur adipiscing elit, sed do eiusmod tempor incididunt ut labore et dolore magna aliqua. Lorem ipsum dolor sit amet, consectetur adipiscing elit, sed do eiusmod tempor incididunt ut labore et dolore magna aliqua. Ut enim ad minim veniam, quis nostrud exercitation ullamco laboris nisi ut aliquip.</p>
  <div class="photo" role="img" aria-label="Hands holding a glowing sphere against a blue background" style="left:200px;top:0;width:190px;height:150px;background:radial-gradient(circle at 50% 45%,#dfeefd,#4b86c4 35%,#173e75 80%)"></div>
  <div class="abs" style="left:200px;top:140px;width:190px;height:52px;background:var(--teal);border-radius:0 0 0 10px;padding:12px 12px;color:#fff;font-size:5.2px;font-weight:700;line-height:1.45">What you are seeking we have a solution, and if we do not, we know someone who will, this is our promise to you!</div>
  <div class="foot-bar"></div><div class="foot-mark">Brightway</div><div class="page-no">PAGE | 13</div>
</section>

<!-- 14 text + brand panel -->
<section class="slide">
  <p class="abs" style="left:20px;top:48px;width:150px;font-size:4.8px;line-height:1.5;color:var(--teal)">Lorem ipsum dolor sit amet, consectetur adipiscing elit, sed do eiusmod tempor incididunt ut labore et dolore magna aliqua. Lorem ipsum dolor sit amet, consectetur adipiscing elit, sed do eiusmod tempor incididunt ut labore et dolore magna aliqua.</p>
  <div class="abs" style="left:20px;top:94px;width:150px">
    <div style="display:grid;grid-template-columns:10px 1fr;row-gap:7px;align-items:start">
      <span style="width:6px;height:6px;border:.8px solid var(--grey);border-radius:50%"></span><p class="body">Lorem ipsum dolor sit amet, consectetur adipiscing elit, sed do eiusmod tempor incididunt ut labore et dolore magna aliqua.</p>
      <span style="width:6px;height:6px;border:.8px solid var(--grey);border-radius:50%"></span><p class="body">Lorem ipsum dolor sit amet, consectetur adipiscing elit, sed do eiusmod tempor incididunt ut labore et dolore magna aliqua.</p>
      <span style="width:6px;height:6px;border:.8px solid var(--grey);border-radius:50%"></span><p class="body">Lorem ipsum dolor sit amet, consectetur adipiscing elit, sed do eiusmod tempor incididunt ut labore et dolore magna aliqua.</p>
      <span style="width:6px;height:6px;border:.8px solid var(--grey);border-radius:50%"></span><p class="body">Lorem ipsum dolor sit amet, consectetur adipiscing elit, sed do eiusmod tempor incididunt ut labore et dolore magna aliqua.</p>
    </div>
  </div>
  <div class="photo" role="img" aria-label="Whiteboard with handwritten leadership notes" style="left:280px;top:0;width:110px;height:219.5px;background:linear-gradient(120deg,#f4f4f4,#d9d9d9)"></div>
  <div class="abs" style="left:185px;top:0;width:125px;height:219.5px;background:var(--teal);display:flex;align-items:center;justify-content:center">
    <div class="display" style="color:#fff;font-size:12px;text-align:center">Brightway<br>&amp; Partners</div>
  </div>
  <div class="foot-bar"></div><div class="foot-mark">Brightway</div><div class="page-no">PAGE | 14</div>
</section>

<!-- 15 core values photos -->
<section class="slide" style="background:var(--teal)">
  <div class="h-title light" style="left:22px;top:98px">Core Values</div>
  <div class="abs" style="left:150px;top:16px;width:106px"><div class="label w">Project name</div><p class="body w" style="font-size:4px">Lorem ipsum dolor sit amet, consectetur adipiscing elit, sed do eiusmod tempor incididunt ut labore et dolore magna aliqua.</p>
    <div class="photo" role="img" aria-label="Laptop with colourful sticky notes" style="position:relative;margin-top:4px;width:82px;height:40px;border-radius:4px;background:linear-gradient(135deg,#e8e8e8,#7fb0d6)"></div></div>
  <div class="abs" style="left:265px;top:16px;width:106px"><div class="label w">Project name</div><p class="body w" style="font-size:4px">Lorem ipsum dolor sit amet, consectetur adipiscing elit, sed do eiusmod tempor incididunt ut labore et dolore magna aliqua.</p>
    <div class="photo" role="img" aria-label="Friends jumping at sunset" style="position:relative;margin-top:4px;width:82px;height:40px;border-radius:4px;background:linear-gradient(180deg,#f2c27a,#c46b2f)"></div></div>
  <div class="abs" style="left:150px;top:116px;width:106px"><div class="label w">Project name</div><p class="body w" style="font-size:4px">Lorem ipsum dolor sit amet, consectetur adipiscing elit, sed do eiusmod tempor incididunt ut labore et dolore magna aliqua.</p>
    <div class="photo" role="img" aria-label="Person on a swing at sunset" style="position:relative;margin-top:4px;width:82px;height:40px;border-radius:4px;background:linear-gradient(180deg,#f7d48a,#6b4a32)"></div></div>
  <div class="abs" style="left:265px;top:116px;width:106px"><div class="label w">Project name</div><p class="body w" style="font-size:4px">Lorem ipsum dolor sit amet, consectetur adipiscing elit, sed do eiusmod tempor incididunt ut labore et dolore magna aliqua.</p>
    <div class="photo" role="img" aria-label="Person in a field under a starry sky" style="position:relative;margin-top:4px;width:82px;height:40px;border-radius:4px;background:linear-gradient(180deg,#2b4c86,#6f86b8 60%,#6b7f3e)"></div></div>
  <div class="foot-bar" style="background:#fff"></div><div class="foot-mark w">Brightway</div><div class="page-no w">PAGE | 15</div>
</section>

<!-- 16 core values text -->
<section class="slide" style="background:var(--teal)">
  <div class="abs" style="left:22px;top:112px;width:70px;height:70px;border-radius:50%;background:rgba(255,255,255,.06)"></div>
  <div class="h-title light" style="left:22px;top:98px">Core Values</div>
  <div class="abs" style="left:155px;top:50px;width:100px"><div class="label w">Project name</div><p class="body w" style="text-align:justify">Lorem ipsum dolor sit amet, consectetur adipiscing elit, sed do eiusmod tempor incididunt ut labore et dolore magna aliqua.</p></div>
  <div class="abs" style="left:270px;top:50px;width:100px"><div class="label w">Project name</div><p class="body w" style="text-align:justify">Lorem ipsum dolor sit amet, consectetur adipiscing elit, sed do eiusmod tempor incididunt ut labore et dolore magna aliqua.</p></div>
  <div class="abs" style="left:155px;top:119px;width:100px"><div class="label w">Project name</div><p class="body w" style="text-align:justify">Lorem ipsum dolor sit amet, consectetur adipiscing elit, sed do eiusmod tempor incididunt ut labore et dolore magna aliqua.</p></div>
  <div class="abs" style="left:270px;top:119px;width:100px"><div class="label w">Project name</div><p class="body w" style="text-align:justify">Lorem ipsum dolor sit amet, consectetur adipiscing elit, sed do eiusmod tempor incididunt ut labore et dolore magna aliqua.</p></div>
  <div class="foot-bar" style="background:#fff"></div><div class="foot-mark w">Brightway</div><div class="page-no w">PAGE | 16</div>
</section>

<!-- 17 vision -->
<section class="slide" style="background:var(--teal)">
  <div class="photo" role="img" aria-label="Wooden letter tiles spelling vision on an orange background" style="left:0;top:24px;width:228px;height:158px;border-radius:0 12px 12px 0;background:linear-gradient(135deg,#f07a4f,#d9b58a 40%,#e8642f)"></div>
  <div class="abs display" style="left:250px;top:78px;color:#fff;font-size:13px">Vision</div>
  <p class="abs body w" style="left:250px;top:100px;width:118px">Lorem ipsum dolor sit amet, consectetur adipiscing elit, sed do eiusmod tempor incididunt ut labore et dolore magna aliqua. Lorem ipsum dolor sit amet, consectetur adipiscing elit.</p>
  <div class="foot-bar" style="background:#fff"></div><div class="foot-mark w">Brightway</div><div class="page-no w">PAGE | 17</div>
</section>

<!-- 18 mission -->
<section class="slide" style="background:var(--teal)">
  <div class="photo" role="img" aria-label="Group of smiling young people outdoors" style="left:0;top:24px;width:216px;height:158px;border-radius:0 12px 12px 0;background:linear-gradient(135deg,#b9c6cf,#8a6e59 50%,#d7c3a6)"></div>
  <div class="abs display" style="left:230px;top:78px;color:#fff;font-size:13px">Mission</div>
  <p class="abs body w" style="left:230px;top:100px;width:130px">Lorem ipsum dolor sit amet, consectetur adipiscing elit, sed do eiusmod tempor incididunt ut labore et dolore magna aliqua. Lorem ipsum dolor sit amet, consectetur adipiscing elit.</p>
  <div class="foot-bar" style="background:#fff"></div><div class="foot-mark w">Brightway</div><div class="page-no w">PAGE | 18</div>
</section>

<!-- 19 icon list -->
<section class="slide">
  <div class="h-title" style="left:38px;top:38px">Here Add Your Title</div>
  <div class="icon-dot" style="left:36px;top:68px"></div>
  <div class="abs" style="left:66px;top:66px;width:90px"><div class="label" style="color:var(--grey)">Project name</div><p class="body">Lorem ipsum dolor sit amet, nec an dictas equidem appellantur, ut has commune accommodare.</p></div>
  <div class="icon-dot" style="left:36px;top:108px"></div>
  <div class="abs" style="left:66px;top:106px;width:90px"><div class="label" style="color:var(--grey)">Project name</div><p class="body">Lorem ipsum dolor sit amet, nec an dictas equidem appellantur, ut has commune accommodare.</p></div>
  <div class="icon-dot" style="left:36px;top:148px"></div>
  <div class="abs" style="left:66px;top:146px;width:90px"><div class="label" style="color:var(--grey)">Project name</div><p class="body">Lorem ipsum dolor sit amet, nec an dictas equidem appellantur, ut has commune accommodare.</p></div>
  <div class="icon-dot" style="left:205px;top:68px"></div>
  <div class="abs" style="left:235px;top:66px;width:90px"><div class="label" style="color:var(--grey)">Project name</div><p class="body">Lorem ipsum dolor sit amet, nec an dictas equidem appellantur, ut has commune accommodare.</p></div>
  <div class="icon-dot" style="left:205px;top:108px"></div>
  <div class="abs" style="left:235px;top:106px;width:90px"><div class="label" style="color:var(--grey)">Project name</div><p class="body">Lorem ipsum dolor sit amet, nec an dictas equidem appellantur, ut has commune accommodare.</p></div>
  <div class="icon-dot" style="left:205px;top:148px"></div>
  <div class="abs" style="left:235px;top:146px;width:90px"><div class="label" style="color:var(--grey)">Project name</div><p class="body">Lorem ipsum dolor sit amet, nec an dictas equidem appellantur, ut has commune accommodare.</p></div>
  <div class="foot-bar"></div><div class="foot-mark">Brightway</div><div class="page-no">PAGE | 19</div>
</section>

<!-- 20 text + photo -->
<section class="slide">
  <div class="h-title" style="left:36px;top:40px">Here Add Your Title</div>
  <p class="abs body" style="left:36px;top:68px;width:145px">Sed do eiusmod tempor incididunt ut labore et dolore magna aliqua. Lorem ipsum dolor sit amet, consectetur adipiscing elit, sed do eiusmod tempor incididunt ut labore et dolore magna aliqua.</p>
  <div class="icon-dot" style="left:36px;top:112px"></div>
  <div class="abs" style="left:66px;top:110px;width:110px"><div class="label" style="color:var(--grey)">Project name</div><p class="body">Lorem ipsum dolor sit amet, nec an dictas equidem appellantur, ut has commune accommodare.</p></div>
  <div class="icon-dot" style="left:36px;top:152px"></div>
  <div class="abs" style="left:66px;top:150px;width:110px"><div class="label" style="color:var(--grey)">Project name</div><p class="body">Lorem ipsum dolor sit amet, nec an dictas equidem appellantur, ut has commune accommodare.</p></div>
  <div class="photo" role="img" aria-label="Hand placing sticky notes on a wall" style="left:224px;top:20px;width:166px;height:199.5px;border-radius:12px 0 0 0;background:linear-gradient(135deg,#f4f4f4,#f7d27b 45%,#f3b86a 70%,#e6e6e6)"></div>
  <div class="foot-bar"></div><div class="foot-mark">Brightway</div><div class="page-no">PAGE | 20</div>
</section>

<!-- 21 road to future -->
<section class="slide">
  <div class="h-title" style="left:18px;top:40px;font-size:13.5px">Road to Your Future</div>
  <p class="abs body" style="left:18px;top:66px;width:150px">Lorem ipsum dolor sit amet, consectetur adipiscing elit, sed do eiusmod tempor incididunt ut labore et dolore magna aliqua. Lorem ipsum dolor sit amet consectetur.</p>
  <div class="photo" role="img" aria-label="Young colleagues laughing around a laptop" style="left:175px;top:20px;width:215px;height:110px;border-radius:12px 0 0 0;background:linear-gradient(135deg,#d9c9b6,#8a6c55 50%,#c9b7a0)"></div>
  <div class="abs" style="left:0;top:146px;width:130px;height:73.5px;background:var(--grey)"></div>
  <div class="abs" style="left:130px;top:146px;width:130px;height:73.5px;background:var(--teal)"></div>
  <div class="abs" style="left:260px;top:146px;width:130px;height:73.5px;background:var(--teal-dark)"></div>
  <div class="icon-dot" style="left:24px;top:134px;width:24px;height:24px;background:var(--grey)"></div>
  <div class="icon-dot" style="left:150px;top:134px;width:24px;height:24px;background:var(--teal)"></div>
  <div class="icon-dot" style="left:286px;top:134px;width:24px;height:24px;background:var(--teal-dark)"></div>
  <div class="abs" style="left:14px;top:168px;width:104px"><div class="label w">Lorem ipsum dolor</div><p class="body w" style="font-size:4px">Lorem ipsum dolor sit amet, consectetur adipiscing elit, sed do eiusmod tempor incididunt ut labore.</p></div>
  <div class="abs" style="left:144px;top:168px;width:104px"><div class="label w">Lorem ipsum dolor</div><p class="body w" style="font-size:4px">Lorem ipsum dolor sit amet, consectetur adipiscing elit, sed do eiusmod tempor incididunt ut labore.</p></div>
  <div class="abs" style="left:274px;top:168px;width:104px"><div class="label w">Lorem ipsum dolor</div><p class="body w" style="font-size:4px">Lorem ipsum dolor sit amet, consectetur adipiscing elit, sed do eiusmod tempor incididunt ut labore.</p></div>
</section>

<!-- 22 table -->
<section class="slide">
  <div class="h-title" style="left:33px;top:34px">Here Add Your Title</div>
  <div class="abs" style="left:33px;top:62px;width:322px;height:86px;display:grid;grid-template-columns:repeat(4,1fr);grid-template-rows:14px 1fr 1fr;background:var(--teal-light)">
    <div style="background:var(--teal);color:#fff;font-size:4.5px;padding:4px 6px;font-weight:600">ADD YOUR TITLE</div>
    <div style="background:var(--teal);color:#fff;font-size:4.5px;padding:4px 6px;font-weight:600">ADD YOUR TITLE</div>
    <div style="background:var(--teal);color:#fff;font-size:4.5px;padding:4px 6px;font-weight:600">ADD YOUR TITLE</div>
    <div style="background:var(--teal);color:#fff;font-size:4.5px;padding:4px 6px;font-weight:600">ADD YOUR TITLE</div>
    <div style="padding:4px 8px"><div class="label">Project name</div><p class="body" style="color:#35615d;font-size:3.8px">Lorem Ipsum is simply dummy unknown printer took a galley of type and scrambled it.</p></div>
    <div style="padding:4px 8px"><div class="label">Project name</div><p class="body" style="color:#35615d;font-size:3.8px">Lorem Ipsum is simply dummy unknown printer took a galley of type and scrambled it.</p></div>
    <div style="padding:4px 8px"><div class="label">Project name</div><p class="body" style="color:#35615d;font-size:3.8px">Lorem Ipsum is simply dummy unknown printer took a galley of type and scrambled it.</p></div>
    <div style="padding:4px 8px"><div class="label">Project name</div><p class="body" style="color:#35615d;font-size:3.8px">Lorem Ipsum is simply dummy unknown printer took a galley of type and scrambled it.</p></div>
    <div style="padding:4px 8px;border-top:.6px solid #fff"><div class="label">Project name</div><p class="body" style="color:#35615d;font-size:3.8px">Lorem Ipsum is simply dummy unknown printer took a galley of type and scrambled it.</p></div>
    <div style="padding:4px 8px;border-top:.6px solid #fff"><div class="label">Project name</div><p class="body" style="color:#35615d;font-size:3.8px">Lorem Ipsum is simply dummy unknown printer took a galley of type and scrambled it.</p></div>
    <div style="padding:4px 8px;border-top:.6px solid #fff"><div class="label">Project name</div><p class="body" style="color:#35615d;font-size:3.8px">Lorem Ipsum is simply dummy unknown printer took a galley of type and scrambled it.</p></div>
    <div style="padding:4px 8px;border-top:.6px solid #fff"><div class="label">Project name</div><p class="body" style="color:#35615d;font-size:3.8px">Lorem Ipsum is simply dummy unknown printer took a galley of type and scrambled it.</p></div>
  </div>
  <div class="foot-bar"></div><div class="foot-mark">Brightway</div><div class="page-no">PAGE | 22</div>
</section>

<!-- 23 photo + teal text -->
<section class="slide" style="background:var(--teal-dark)">
  <div class="photo" role="img" aria-label="Chess king piece at sunset" style="left:0;top:18px;width:176px;height:201.5px;border-radius:0 14px 0 0;background:linear-gradient(180deg,#b3c2d3,#f1c07a 55%,#7a5130)"></div>
  <div class="abs display" style="left:190px;top:66px;color:#fff;font-size:13px">Here Add Your Title</div>
  <p class="abs body w" style="left:190px;top:92px;width:180px">Lorem ipsum dolor sit amet, consectetur adipiscing elit, sed do eiusmod tempor incididunt ut labore et dolore magna aliqua. Lorem ipsum dolor sit amet, consectetur adipiscing elit, sed do eiusmod tempor incididunt ut labore et dolore magna aliqua.<br><br>Lorem ipsum dolor sit amet, consectetur adipiscing elit, sed do eiusmod tempor incididunt ut labore et dolore magna aliqua. Lorem ipsum dolor sit amet.</p>
</section>

<!-- 24 phone features -->
<section class="slide">
  <div class="h-title" style="left:28px;top:30px">Here Add Your Title</div>
  <div class="photo" role="img" aria-label="Smartphone showing the coaching app screen" style="left:162px;top:52px;width:62px;height:126px;border-radius:9px;background:linear-gradient(180deg,#2b2b2b,#111);padding:4px"><div style="width:100%;height:100%;border-radius:6px;background:linear-gradient(180deg,#f5f5f5,#e3e3e3)"></div></div>
  <svg class="abs" style="inset:0" width="390" height="219.5" fill="none" stroke="#9a9a9a" stroke-width=".5" stroke-dasharray="1.5 1.5">
    <path d="M120 90 H165"/><path d="M120 147 H165"/><path d="M222 80 H295 V72"/><path d="M222 130 H290 V124"/><path d="M222 160 H270 V170"/>
  </svg>
  <div class="abs" style="left:50px;top:74px;width:110px;text-align:center;font-size:5.5px;color:var(--coral)">Mix of methods, e.g. micro impulses, contemplation, tests, peer feedback</div>
  <div class="abs" style="left:45px;top:138px;width:115px;text-align:center;font-size:5.5px;color:var(--teal)">Content collection including models, methods and exercises</div>
  <div class="abs" style="left:262px;top:58px;width:90px;text-align:center;font-size:5.5px;color:var(--coral)">Individualised coaching journey</div>
  <div class="abs" style="left:262px;top:112px;width:90px;text-align:center;font-size:5.5px;color:var(--teal)">Contact coaching and IT support</div>
  <div class="abs" style="left:250px;top:172px;width:90px;text-align:center;font-size:5.5px;color:var(--teal)">All insights in one place</div>
  <div class="foot-bar"></div><div class="foot-mark">Brightway</div><div class="page-no">PAGE | 24</div>
</section>

<!-- 25 timeline -->
<section class="slide">
  <div class="h-title" style="left:28px;top:34px">Timeline</div>
  <svg class="abs" style="left:0;top:0" width="390" height="219.5">
    <g font-family="Open Sans,sans-serif" font-size="5" font-weight="700" fill="#fff" text-anchor="middle">
      <polygon points="44,126 112,126 118,131 112,136 44,136 38,131" fill="#0b5f5a"/><text x="78" y="133">1990</text>
      <polygon points="107,126 170,126 176,131 170,136 107,136 113,131" fill="#6d6d6d"/><text x="141" y="133">2001</text>
      <polygon points="165,126 234,126 240,131 234,136 165,136 171,131" fill="#0b5f5a"/><text x="202" y="133">2007</text>
      <polygon points="229,126 296,126 302,131 296,136 229,136 235,131" fill="#6d6d6d"/><text x="265" y="133">2012</text>
      <polygon points="291,126 360,126 366,131 360,136 291,136 297,131" fill="#0b5f5a"/><text x="328" y="133">2020</text>
    </g>
    <g stroke="#0b5f5a" stroke-width=".8"><line x1="78" y1="110" x2="78" y2="126"/><line x1="202" y1="110" x2="202" y2="126"/><line x1="328" y1="110" x2="328" y2="126"/><line x1="141" y1="136" x2="141" y2="150"/><line x1="265" y1="136" x2="265" y2="150"/></g>
    <g fill="#0b5f5a"><circle cx="78" cy="122" r="2"/><circle cx="202" cy="122" r="2"/><circle cx="328" cy="122" r="2"/><circle cx="141" cy="150" r="2"/><circle cx="265" cy="150" r="2"/></g>
  </svg>
  <div class="abs" style="left:48px;top:88px;width:60px;text-align:center;font-size:4.5px;color:var(--ink)">Your Title<div class="body" style="font-size:3.8px">Refers to a good or service being offered</div></div>
  <div class="abs" style="left:172px;top:88px;width:60px;text-align:center;font-size:4.5px;color:var(--ink)">Your Title<div class="body" style="font-size:3.8px">Refers to a good or service being offered</div></div>
  <div class="abs" style="left:298px;top:88px;width:60px;text-align:center;font-size:4.5px;color:var(--ink)">Your Title<div class="body" style="font-size:3.8px">Refers to a good or service being offered</div></div>
  <div class="abs" style="left:111px;top:156px;width:60px;text-align:center;font-size:4.5px;color:var(--ink)">Your Title<div class="body" style="font-size:3.8px">Refers to a good or service being offered</div></div>
  <div class="abs" style="left:235px;top:156px;width:60px;text-align:center;font-size:4.5px;color:var(--ink)">Your Title<div class="body" style="font-size:3.8px">Refers to a good or service being offered</div></div>
  <div class="foot-bar"></div><div class="foot-mark">Brightway</div><div class="page-no">PAGE | 25</div>
</section>

<!-- 26 clients -->
<section class="slide">
  <div class="abs display" style="left:34px;top:52px;font-size:13px;color:var(--grey);line-height:1.25">We Have<br>Worked With…</div>
  <div class="abs" style="left:200px;top:62px;display:grid;grid-template-columns:repeat(2,80px);column-gap:6px;font-family:'Comfortaa',sans-serif;font-weight:700;font-size:8px;color:var(--grey);text-align:center">
    <span>Northmarket</span><span>Vantra</span>
  </div>
  <div class="abs" style="left:150px;top:104px;display:grid;grid-template-columns:repeat(2,80px);column-gap:6px;font-family:'Comfortaa',sans-serif;font-weight:700;font-size:8px;color:var(--grey);text-align:center">
    <span>Holmbo</span><span>Qadira</span>
  </div>
  <div class="abs" style="left:110px;top:146px;display:grid;grid-template-columns:repeat(2,100px);column-gap:6px;font-family:'Comfortaa',sans-serif;font-weight:700;font-size:8px;color:var(--grey);text-align:center">
    <span>Corelane</span><span>Meshwork</span>
  </div>
  <div class="foot-bar"></div><div class="foot-mark">Brightway</div><div class="page-no">PAGE | 26</div>
</section>

<!-- 27 box grid -->
<section class="slide">
  <div class="h-title" style="left:24px;top:18px">Here Add Your Title</div>
  <div class="tile" style="left:16px;top:46px;width:66px;height:80px"></div>
  <div class="tile" style="left:88px;top:46px;width:172px;height:44px"></div>
  <div class="tile" style="left:266px;top:46px;width:108px;height:80px"></div>
  <div class="tile" style="left:88px;top:96px;width:78px;height:48px"></div>
  <div class="tile" style="left:172px;top:96px;width:88px;height:48px"></div>
  <div class="tile" style="left:16px;top:132px;width:66px;height:70px"></div>
  <div class="tile" style="left:88px;top:150px;width:172px;height:52px"></div>
  <div class="tile" style="left:266px;top:132px;width:108px;height:70px"></div>
  <div class="abs brand" style="left:6px;top:208px;font-size:4.5px">Brightway &amp; Partners</div>
  <div class="page-no">PAGE | 27</div>
</section>

<!-- 28 team -->
<section class="slide">
  <div class="h-title" style="left:40px;top:20px">Our Team</div>
  <div class="abs" style="left:40px;top:46px;width:300px;display:grid;grid-template-columns:repeat(4,64px);grid-template-rows:repeat(2,72px);gap:6px 14px">
    <div class="card" style="position:relative;padding:4px"><div class="label t" style="text-align:center;font-size:3.8px">Your Name</div><div style="display:flex;gap:3px;margin-top:4px"><span style="width:14px;height:14px;border-radius:50%;background:var(--grey-light);flex:none"></span><span class="body" style="font-size:3px">Founding Partner, Chairman</span></div><p class="body" style="font-size:3px;margin-top:4px;color:#555">Maecenas in porta et tellus incidunt suitable ex sed nibh diam.</p></div>
    <div class="card" style="position:relative;padding:4px"><div class="label t" style="text-align:center;font-size:3.8px">Your Name</div><div style="display:flex;gap:3px;margin-top:4px"><span style="width:14px;height:14px;border-radius:50%;background:var(--grey-light);flex:none"></span><span class="body" style="font-size:3px">Founding Partner, Chairman</span></div><p class="body" style="font-size:3px;margin-top:4px;color:#555">Maecenas in porta et tellus incidunt suitable ex sed nibh diam.</p></div>
    <div class="card" style="position:relative;padding:4px"><div class="label t" style="text-align:center;font-size:3.8px">Your Name</div><div style="display:flex;gap:3px;margin-top:4px"><span style="width:14px;height:14px;border-radius:50%;background:var(--grey-light);flex:none"></span><span class="body" style="font-size:3px">Founding Partner, Chairman</span></div><p class="body" style="font-size:3px;margin-top:4px;color:#555">Maecenas in porta et tellus incidunt suitable ex sed nibh diam.</p></div>
    <div class="card" style="position:relative;padding:4px"><div class="label t" style="text-align:center;font-size:3.8px">Your Name</div><div style="display:flex;gap:3px;margin-top:4px"><span style="width:14px;height:14px;border-radius:50%;background:var(--grey-light);flex:none"></span><span class="body" style="font-size:3px">Founding Partner, Chairman</span></div><p class="body" style="font-size:3px;margin-top:4px;color:#555">Maecenas in porta et tellus incidunt suitable ex sed nibh diam.</p></div>
    <div class="card" style="position:relative;padding:4px"><div class="label t" style="text-align:center;font-size:3.8px">Your Name</div><div style="display:flex;gap:3px;margin-top:4px"><span style="width:14px;height:14px;border-radius:50%;background:var(--grey-light);flex:none"></span><span class="body" style="font-size:3px">Founding Partner, Chairman</span></div><p class="body" style="font-size:3px;margin-top:4px;color:#555">Maecenas in porta et tellus incidunt suitable ex sed nibh diam.</p></div>
    <div class="card" style="position:relative;padding:4px"><div class="label t" style="text-align:center;font-size:3.8px">Your Name</div><div style="display:flex;gap:3px;margin-top:4px"><span style="width:14px;height:14px;border-radius:50%;background:var(--grey-light);flex:none"></span><span class="body" style="font-size:3px">Founding Partner, Chairman</span></div><p class="body" style="font-size:3px;margin-top:4px;color:#555">Maecenas in porta et tellus incidunt suitable ex sed nibh diam.</p></div>
    <div class="card" style="position:relative;padding:4px"><div class="label t" style="text-align:center;font-size:3.8px">Your Name</div><div style="display:flex;gap:3px;margin-top:4px"><span style="width:14px;height:14px;border-radius:50%;background:var(--grey-light);flex:none"></span><span class="body" style="font-size:3px">Founding Partner, Chairman</span></div><p class="body" style="font-size:3px;margin-top:4px;color:#555">Maecenas in porta et tellus incidunt suitable ex sed nibh diam.</p></div>
    <div class="card" style="position:relative;padding:4px"><div class="label t" style="text-align:center;font-size:3.8px">Your Name</div><div style="display:flex;gap:3px;margin-top:4px"><span style="width:14px;height:14px;border-radius:50%;background:var(--grey-light);flex:none"></span><span class="body" style="font-size:3px">Founding Partner, Chairman</span></div><p class="body" style="font-size:3px;margin-top:4px;color:#555">Maecenas in porta et tellus incidunt suitable ex sed nibh diam.</p></div>
  </div>
  <div class="foot-bar"></div><div class="foot-mark">Brightway</div><div class="page-no">PAGE | 28</div>
</section>

<!-- 29 venn -->
<section class="slide">
  <div class="abs display" style="left:30px;top:64px;font-size:13px;color:var(--grey);line-height:1.2">Venn<br>diagram</div>
  <p class="abs body" style="left:30px;top:108px;width:150px;font-size:4.6px;line-height:1.9">Laoreet copiosae recusabo cu sed, mel ad alia tritani ponderum. Pri impetus ceteros fierent at, mel id magna causae accusamus, tota appetere at mei.</p>
  <svg class="abs" style="left:0;top:0" width="390" height="219.5">
    <defs><clipPath id="venn-left"><circle cx="263" cy="110" r="52"/></clipPath></defs>
    <circle cx="263" cy="110" r="52" fill="#0f7f78"/>
    <circle cx="327" cy="110" r="52" fill="#f36b4b"/>
    <circle cx="327" cy="110" r="52" fill="#6b4236" clip-path="url(#venn-left)"/>
    <g font-family="Open Sans,sans-serif" font-size="4" fill="#fff" text-anchor="middle">
      <text x="245" y="94">Item 01</text><text x="245" y="108">Item 02</text><text x="245" y="122">Item 03</text>
      <text x="295" y="94">Item 04</text><text x="295" y="108">Item 05</text><text x="295" y="122">Item 06</text>
      <text x="345" y="94">Item 07</text><text x="345" y="108">Item 08</text><text x="345" y="122">Item 09</text>
    </g>
  </svg>
  <div class="foot-bar"></div><div class="foot-mark">Brightway</div><div class="page-no">PAGE | 29</div>
</section>

<!-- 30 nested circles -->
<section class="slide">
  <div class="h-title" style="left:34px;top:20px">Here Add Your Title</div>
  <svg class="abs" style="left:0;top:0" width="390" height="219.5">
    <circle cx="88" cy="116" r="55" fill="#0b5f5a"/>
    <circle cx="88" cy="133" r="38" fill="#0f7f78"/>
    <circle cx="88" cy="152" r="19" fill="#f36b4b"/>
    <g font-family="Comfortaa,sans-serif" font-size="11" fill="#fff" text-anchor="middle" font-weight="700"><text x="88" y="81">$</text><text x="88" y="119">$</text><text x="88" y="156" font-size="8">$</text></g>
    <g stroke="#555" stroke-width=".5"><line x1="98" y1="77" x2="160" y2="77"/><line x1="98" y1="116" x2="160" y2="116"/><line x1="98" y1="152" x2="160" y2="152"/></g>
    <g font-family="Open Sans,sans-serif" font-size="8" fill="#3a3a3a"><text x="162" y="80">999M</text><text x="162" y="119">99M</text><text x="162" y="155">9M</text></g>
    <circle cx="248" cy="76" r="8" fill="#0b5f5a"/><path d="M244 76 l3 3 l5 -6" stroke="#fff" stroke-width="1.4" fill="none"/>
    <circle cx="248" cy="114" r="8" fill="#0f7f78"/><path d="M244 114 l3 3 l5 -6" stroke="#fff" stroke-width="1.4" fill="none"/>
    <circle cx="248" cy="152" r="8" fill="#f36b4b"/><path d="M244 152 l3 3 l5 -6" stroke="#fff" stroke-width="1.4" fill="none"/>
  </svg>
  <div class="abs" style="left:262px;top:66px;width:100px"><div class="label" style="font-size:4.2px;font-weight:400">Lorem ipsum dolor</div><p class="body" style="font-size:4px">Lorem ipsum dolor sit amet, consectetur adipiscing elit, sed do eiusmod tempor</p></div>
  <div class="abs" style="left:262px;top:104px;width:100px"><div class="label" style="font-size:4.2px;font-weight:400">Lorem ipsum dolor</div><p class="body" style="font-size:4px">Lorem ipsum dolor sit amet, consectetur adipiscing elit, sed do eiusmod tempor</p></div>
  <div class="abs" style="left:262px;top:142px;width:100px"><div class="label" style="font-size:4.2px;font-weight:400">Lorem ipsum dolor</div><p class="body" style="font-size:4px">Lorem ipsum dolor sit amet, consectetur adipiscing elit, sed do eiusmod tempor</p></div>
  <div class="foot-bar"></div><div class="foot-mark">Brightway</div><div class="page-no">PAGE | 30</div>
</section>

<!-- 31 triangle -->
<section class="slide">
  <div class="h-title" style="left:38px;top:24px">Here Add Your Title</div>
  <div class="icon-dot" style="left:38px;top:62px;background:var(--coral)"></div>
  <div class="abs" style="left:66px;top:60px;width:100px"><div class="label" style="color:var(--grey)">Project name</div><p class="body">Lorem ipsum dolor sit amet, nec an dictas equidem appellantur, ut has commune.</p></div>
  <div class="icon-dot" style="left:38px;top:102px"></div>
  <div class="abs" style="left:66px;top:100px;width:100px"><div class="label" style="color:var(--grey)">Project name</div><p class="body">Lorem ipsum dolor sit amet, nec an dictas equidem appellantur, ut has commune.</p></div>
  <div class="icon-dot" style="left:38px;top:142px;background:var(--grey)"></div>
  <div class="abs" style="left:66px;top:140px;width:100px"><div class="label" style="color:var(--grey)">Project name</div><p class="body">Lorem ipsum dolor sit amet, nec an dictas equidem appellantur, ut has commune.</p></div>
  <svg class="abs" style="left:0;top:0" width="390" height="219.5">
    <polygon points="272,40 305,98 239,98" fill="#f36b4b" stroke="#fff" stroke-width="2" stroke-linejoin="round"/>
    <polygon points="239,98 272,156 206,156" fill="#0b5f5a" stroke="#fff" stroke-width="2" stroke-linejoin="round"/>
    <polygon points="305,98 338,156 272,156" fill="#0b5f5a" stroke="#fff" stroke-width="2" stroke-linejoin="round"/>
    <g font-family="Open Sans,sans-serif" font-size="3.6" fill="#fff" text-anchor="middle">
      <text x="272" y="76" font-weight="700">Project name</text><text x="272" y="82">Lorem ipsum dolor sit</text><text x="272" y="87">amet nec dictas</text>
      <text x="246" y="130" font-weight="700">Project name</text><text x="246" y="136">Lorem ipsum dolor</text><text x="246" y="141">sit amet dictas</text>
      <text x="305" y="130" font-weight="700">Project name</text><text x="305" y="136">Lorem ipsum dolor</text><text x="305" y="141">sit amet dictas</text>
    </g>
  </svg>
  <div class="foot-bar"></div><div class="foot-mark">Brightway</div><div class="page-no">PAGE | 31</div>
</section>

<!-- 32 ring -->
<section class="slide">
  <div class="h-title" style="left:34px;top:20px">Here Add Your Title</div>
  <svg class="abs" style="left:0;top:0" width="390" height="219.5">
    <g transform="rotate(-90 195 112)" fill="none" stroke-width="18">
      <circle cx="195" cy="112" r="36" stroke="#0b5f5a" stroke-dasharray="56.5 169.6" stroke-dashoffset="0"/>
      <circle cx="195" cy="112" r="36" stroke="#0f7f78" stroke-dasharray="56.5 169.6" stroke-dashoffset="-56.5"/>
      <circle cx="195" cy="112" r="36" stroke="#6d6d6d" stroke-dasharray="56.5 169.6" stroke-dashoffset="-113.1"/>
      <circle cx="195" cy="112" r="36" stroke="#f36b4b" stroke-dasharray="56.5 169.6" stroke-dashoffset="-169.6"/>
    </g>
    <g stroke="#fff" stroke-width="2"><line x1="195" y1="67" x2="195" y2="85"/><line x1="195" y1="139" x2="195" y2="157"/><line x1="150" y1="112" x2="168" y2="112"/><line x1="222" y1="112" x2="240" y2="112"/></g>
    <g fill="#fff"><circle cx="220" cy="87" r="4"/><circle cx="220" cy="137" r="4"/><circle cx="170" cy="137" r="4"/><circle cx="170" cy="87" r="4"/></g>
  </svg>
  <div class="abs brand" style="left:175px;top:106px;width:40px;text-align:center;font-size:4.4px">Brightway &amp; Partners</div>
  <div class="abs" style="left:40px;top:70px;width:90px;text-align:right"><div class="label" style="font-weight:400;font-size:4.5px">Your Contents Here</div><p class="body" style="font-size:4px">Lorem ipsum dolor sit amet, consectetur adipiscing elit, sed do eiusmod tempor incididunt</p></div>
  <div class="abs" style="left:40px;top:138px;width:90px;text-align:right"><div class="label" style="font-weight:400;font-size:4.5px">Your Contents Here</div><p class="body" style="font-size:4px">Lorem ipsum dolor sit amet, consectetur adipiscing elit, sed do eiusmod tempor incididunt</p></div>
  <div class="abs" style="left:262px;top:70px;width:90px"><div class="label" style="font-weight:400;font-size:4.5px">Your Contents Here</div><p class="body" style="font-size:4px">Lorem ipsum dolor sit amet, consectetur adipiscing elit, sed do eiusmod tempor incididunt</p></div>
  <div class="abs" style="left:262px;top:136px;width:90px"><div class="label" style="font-weight:400;font-size:4.5px">Your Contents Here</div><p class="body" style="font-size:4px">Lorem ipsum dolor sit amet, consectetur adipiscing elit, sed do eiusmod tempor incididunt</p></div>
  <div class="foot-bar"></div><div class="foot-mark">Brightway</div><div class="page-no">PAGE | 32</div>
</section>

<!-- 33 bar chart -->
<section class="slide">
  <svg class="abs" style="left:0;top:0" width="390" height="219.5">
    <line x1="30" y1="168" x2="160" y2="168" stroke="#ccc" stroke-width=".5"/>
    <rect x="38" y="68" width="12" height="100" fill="#0b5f5a"/>
    <rect x="72" y="130" width="12" height="38" fill="#f36b4b"/>
    <rect x="106" y="103" width="12" height="65" fill="#0b5f5a"/>
    <rect x="140" y="148" width="12" height="20" fill="#6d6d6d"/>
    <g font-family="Open Sans,sans-serif" font-size="3.6" fill="#fff" text-anchor="middle" font-weight="700">
      <rect x="39" y="57" width="10" height="7" rx="1" fill="#0b5f5a"/><text x="44" y="62">80</text>
      <rect x="73" y="119" width="10" height="7" rx="1" fill="#0b5f5a"/><text x="78" y="124">35</text>
      <rect x="107" y="92" width="10" height="7" rx="1" fill="#0b5f5a"/><text x="112" y="97">55</text>
      <rect x="141" y="137" width="10" height="7" rx="1" fill="#0b5f5a"/><text x="146" y="142">10</text>
    </g>
    <g font-family="Open Sans,sans-serif" font-size="3.4" fill="#888" text-anchor="middle"><text x="44" y="175">Category 1</text><text x="78" y="175">Category 2</text><text x="112" y="175">Category 3</text><text x="146" y="175">Category 4</text></g>
  </svg>
  <div class="h-title" style="left:210px;top:38px">Here Add Your Title</div>
  <div class="abs" style="left:210px;top:70px;width:150px;display:grid;grid-template-columns:10px 1fr;row-gap:6px">
    <span style="width:5px;height:5px;border:.8px solid var(--grey);border-radius:50%"></span><p class="body" style="font-size:4px">Lorem ipsum dolor sit amet, consectetur adipiscing elit, sed do eiusmod tempor incididunt ut labore et dolore magna aliqua.</p>
    <span style="width:5px;height:5px;border:.8px solid var(--grey);border-radius:50%"></span><p class="body" style="font-size:4px">Lorem ipsum dolor sit amet, consectetur adipiscing elit, sed do eiusmod tempor incididunt ut labore et dolore magna aliqua.</p>
    <span style="width:5px;height:5px;border:.8px solid var(--grey);border-radius:50%"></span><p class="body" style="font-size:4px">Lorem ipsum dolor sit amet, consectetur adipiscing elit, sed do eiusmod tempor incididunt ut labore et dolore magna aliqua.</p>
    <span style="width:5px;height:5px;border:.8px solid var(--grey);border-radius:50%"></span><p class="body" style="font-size:4px">Lorem ipsum dolor sit amet, consectetur adipiscing elit, sed do eiusmod tempor incididunt ut labore et dolore magna aliqua.</p>
  </div>
  <div class="foot-bar"></div><div class="foot-mark">Brightway</div><div class="page-no">PAGE | 33</div>
</section>

<!-- 34 gauges -->
<section class="slide">
  <div class="abs display" style="left:0;right:0;top:30px;text-align:center;font-size:14px;color:var(--ink)">Here Add Your Title</div>
  <p class="abs body" style="left:85px;top:56px;width:220px;text-align:center">Lorem Ipsum the printing and typesetting industry. Lorem Ipsum has been the industry's standard dummy text ever since the 1500s, when an unknown printer took a galley of type and scrambled it to make a type specimen book. It has survived not only five centuries.</p>
  <svg class="abs" style="left:0;top:0" width="390" height="219.5">
    <g fill="none" stroke-width="4">
      <circle cx="110" cy="132" r="20" stroke="#e3e3e3"/><circle cx="110" cy="132" r="20" stroke="#0b5f5a" stroke-dasharray="62.8 125.7" transform="rotate(-90 110 132)" stroke-linecap="round"/>
      <circle cx="195" cy="132" r="20" stroke="#e3e3e3"/><circle cx="195" cy="132" r="20" stroke="#0f7f78" stroke-dasharray="94.2 125.7" transform="rotate(-90 195 132)" stroke-linecap="round"/>
      <circle cx="280" cy="132" r="20" stroke="#e3e3e3"/><circle cx="280" cy="132" r="20" stroke="#f36b4b" stroke-dasharray="50.3 125.7" transform="rotate(-90 280 132)" stroke-linecap="round"/>
    </g>
    <g font-family="Comfortaa,sans-serif" font-size="11" font-weight="700" fill="#555" text-anchor="middle"><text x="110" y="136">50%</text><text x="195" y="136">75%</text><text x="280" y="136">40%</text></g>
  </svg>
  <p class="abs body" style="left:80px;top:162px;width:60px;text-align:center;font-size:3.8px">Lorem ipsum dolor amet consectetur dolor</p>
  <p class="abs body" style="left:165px;top:162px;width:60px;text-align:center;font-size:3.8px">Lorem ipsum dolor amet consectetur dolor</p>
  <p class="abs body" style="left:250px;top:162px;width:60px;text-align:center;font-size:3.8px">Lorem ipsum dolor amet consectetur dolor</p>
  <div class="foot-bar"></div><div class="foot-mark">Brightway</div><div class="page-no">PAGE | 34</div>
</section>

<!-- 35 line + pie -->
<section class="slide">
  <div class="h-title" style="left:24px;top:26px">Here Add Your Title</div>
  <div class="abs" style="left:24px;top:72px;font-size:4px;color:var(--ink)">Line Graph #1<div style="font-size:3.2px;color:#999">(Subtitle Details)</div></div>
  <div class="abs" style="left:230px;top:72px;font-size:4px;color:var(--ink)">Pie Chart #1<div style="font-size:3.2px;color:#999">(Subtitle Details)</div></div>
  <svg class="abs" style="left:0;top:0" width="390" height="219.5">
    <polyline points="30,150 42,138 54,160 66,140 80,110 94,150 108,135 122,165 136,128 150,140 164,100 176,135" fill="none" stroke="#f36b4b" stroke-width="1.4"/>
    <polyline points="30,140 44,160 58,130 72,150 86,160 100,120 114,150 128,140 142,160 156,130 170,110 178,118" fill="none" stroke="#0b5f5a" stroke-width="1.4"/>
    <g font-family="Open Sans,sans-serif" font-size="3.2" fill="#888"><text x="26" y="180">2005</text><text x="46" y="180">2006</text><text x="66" y="180">2007</text><text x="86" y="180">2008</text><text x="106" y="180">2009</text><text x="126" y="180">2010</text><text x="146" y="180">2011</text><text x="166" y="180">2012</text><text x="184" y="180">2013</text></g>
    <g fill="none" stroke-width="16" transform="rotate(-90 285 132)">
      <circle cx="285" cy="132" r="30" stroke="#0b5f5a" stroke-dasharray="94.2 188.5"/>
      <circle cx="285" cy="132" r="30" stroke="#f36b4b" stroke-dasharray="75.4 188.5" stroke-dashoffset="-94.2"/>
      <circle cx="285" cy="132" r="30" stroke="#0f7f78" stroke-dasharray="18.9 188.5" stroke-dashoffset="-169.6"/>
    </g>
    <g font-family="Open Sans,sans-serif" font-size="4" fill="#fff" font-weight="700" text-anchor="middle"><text x="310" y="114">50</text><text x="285" y="166">40</text><text x="258" y="122">20</text></g>
  </svg>
  <div class="foot-bar"></div><div class="foot-mark">Brightway</div><div class="page-no">PAGE | 35</div>
</section>

<!-- 36 closing -->
<section class="slide">
  <div class="photo" role="img" aria-label="Team working together in an office, dark teal tint" style="inset:0;background:linear-gradient(160deg,#0f5e59,#0b4d49 50%,#0a423f)"></div>
  <div class="abs brand" style="left:0;right:0;top:76px;text-align:center;font-size:17px;color:#fff">Brightway &amp; Partners<small style="font-size:.3em">COACHING, CONSULTING UND EXECUTIVE SEARCH</small></div>
  <div class="abs display" style="left:0;right:0;top:148px;text-align:center;font-size:14px;color:#fff">Thank You. <span style="color:var(--coral)">Contact Us.</span></div>
  <div class="abs" style="left:36px;right:20px;top:188px;display:flex;justify-content:space-between;font-size:4px;color:rgba(255,255,255,.85)">
    <span>&#9711; www.brightway-partners.de</span>
    <span>&#9679; Lindenstraße 12, 80331 München</span>
    <span>&#9742; +49 89 123 456 0</span>
    <span>&#9993; info@brightway-partners.de</span>
  </div>
</section>

</main>
</body>
</html>
```